Marketing Flyer for Office Space for Lease

I am looking for a pretty standard and professional real estate flyer listing my property for lease. I am not looking for anything over the top creative, just something very professional looking. The building address is 4817 E. Calloway Avenue, Lauderhill, FL 33319. I included some sample flyers of what other companies use as examples on what I am looking for. Please use the attached Dorvel Holdings Realty logo, but remove the long line after it extends past the words. I also included a Word file that gives you the building information and marketing information. Please use the photos attached in the zipped folder as you see fit.
Updates

Project Deadline Extended
Reason: I am getting updated building measurements next Thursday. I want to be able to give these figures to you to ensure the flyer is final. I will keep making comments on the rest of the designs while I wait for those numbers. Thank you.

Project Deadline Extended
Reason: Just got the floor plans, so I needed to adjust the figures on the flyer. Otherwise I would just have an incorrect flyer.

Target Market(s)

Businesses that would want to lease space in this building.

Industry/Entity Type

Real Estate

Font styles to use
Serif
Sans Serif

Colors

Designer to choose colors to be used in the design.

Requirements
Must have
• Building photo, address, map, and building highlights from the Word file.
Nice to have
• I included the example flyers that I have seen or used in the past. Taking ideas from there could work well.
Should not have
• Crazy big fonts, crazy colors, hard to read fonts, too wild of layout.

```html
<!DOCTYPE html>
<html lang="en">
<head>
<meta charset="utf-8">
<title>Office Space For Lease – Flyer</title>
<link href="https://fonts.googleapis.com/css2?family=Archivo+Black&family=Cinzel:wght@400;600&family=Raleway:wght@300;400;500;700&display=swap" rel="stylesheet">
<style>
  :root{
    --backdrop:#8f8f8f;
    --paper:#ffffff;
    --brand-blue:#0b4f96;
    --band-blue:#2d5fa6;
    --panel-blue:#1f4f98;
    --rule-blue:#3d8be0;
    --slate:#5d5f63;
    --ink:#5a5a5a;
    --ink-soft:#6e6e6e;
    --sky:#5f9bd8;
    --sky-light:#cfe0f2;
    --wall:#e9ecef;
    --lawn:#4f6a3a;
    --asphalt:#55595e;
  }
  *{box-sizing:border-box;margin:0;padding:0}
  html,body{width:1200px;height:1200px;overflow:hidden;background:var(--backdrop)}
  body{position:relative;font-family:"Raleway",sans-serif;font-variant-numeric:lining-nums;font-feature-settings:"lnum" 1}
  .sheet{position:absolute;top:254px;width:534px;height:692px;background:var(--paper);overflow:hidden}
  .sheet--front{left:63px}
  .sheet--back{left:603px}
  .photo{position:absolute;background:linear-gradient(180deg,var(--sky) 0%,var(--sky-light) 30%,var(--wall) 50%,var(--wall) 65%,var(--asphalt) 82%,var(--lawn) 100%)}
  .photo--aerial{background:linear-gradient(180deg,var(--lawn) 0%,var(--wall) 35%,var(--wall) 60%,var(--asphalt) 85%,var(--lawn) 100%)}

  /* front */
  .hero{left:0;top:0;width:534px;height:414px}
  .headline{position:absolute;left:30px;top:262px;font-family:"Archivo Black",sans-serif;color:#fff;line-height:.86;letter-spacing:-3px}
  .headline__small{display:block;font-size:50px}
  .headline__big{display:block;font-size:84px;letter-spacing:-5px}
  .front-shapes{position:absolute;left:0;top:383px;width:534px;height:110px}
  .info-title{position:absolute;left:32px;top:391px;font-family:"Cinzel",serif;font-weight:600;font-size:16px;letter-spacing:1px;color:#fff}
  .specs{position:absolute;left:31px;top:421px;color:#fff;border-collapse:collapse}
  .specs th{font-weight:700;text-align:left;font-size:10px;width:111px;padding:2px 0 3px;white-space:nowrap}
  .specs td{font-weight:400;font-size:12.5px;padding:2px 0 3px;white-space:nowrap}
  .specs sup{font-size:6px}
  .front-address{position:absolute;left:273px;top:446px;color:#fff;font-size:10.5px;display:flex;align-items:center;gap:5px;white-space:nowrap}
  .strip{position:absolute;left:0;top:491px;width:534px;height:121px}
  .strip svg{width:100%;height:100%}
  .front-contact{position:absolute;left:0;top:612px;width:534px;height:80px;display:flex;align-items:center;justify-content:space-between;padding:0 30px;color:var(--ink)}
  .front-contact__item{display:flex;align-items:center;gap:7px;white-space:nowrap}
  .front-contact__phone{font-weight:700;font-size:20px}
  .front-contact__email{font-weight:400;font-size:21px;color:var(--ink-soft)}

  /* back */
  .col-left{position:absolute;left:0;width:190px}
  .top-left{top:0;height:136px}
  .top-right{left:190px;top:0;width:344px;height:136px}
  .title-block{top:136px;height:200px;background:var(--brand-blue)}
  .title-block__heading{position:absolute;left:33px;top:24px;font-family:"Cinzel",serif;font-weight:400;color:#fff;font-size:46px;line-height:.98;letter-spacing:1px}
  .title-block__rule{position:absolute;left:0;top:122px;width:190px;height:2px;background:var(--rule-blue)}
  .title-block__address{position:absolute;left:31px;top:136px;display:flex;gap:6px;color:#fff;font-size:12px;line-height:1.3}
  .mid-left{top:335px;height:221px}
  .brand-block{top:556px;height:136px;background:var(--brand-blue);padding:16px 0 0 34px;color:#fff}
  .brand-name{font-family:"Raleway",sans-serif;font-weight:700;font-size:19px;line-height:1.15;color:#fff;width:140px}
  .brand-block__phone{margin-top:16px;font-size:14px;white-space:nowrap}
  .brand-block__email{font-size:10px;margin-top:1px;white-space:nowrap}
  .bottom-right{left:190px;top:556px;width:344px;height:136px}
  .features{position:absolute;left:190px;top:136px;width:344px;height:420px;padding:22px 28px 0 27px}
  .features__title{font-weight:700;font-size:22px;line-height:1.14;color:var(--brand-blue);margin-bottom:7px}
  .features__list{list-style:none;font-size:10.4px;font-weight:400;color:var(--ink-soft);line-height:1.22}
  .features__list > li{display:flex;gap:6px;margin-bottom:8px}
  .features__list svg{flex:none;margin-top:1px}
  .features__sub{list-style:none;margin-top:5px}
  .features__sub li{position:relative;padding-left:12px;margin-bottom:3.5px}
  .features__sub li::before{content:"·";position:absolute;left:0}
</style>
</head>
<body>
<svg width="0" height="0" style="position:absolute">
  <defs>
    <symbol id="tick" viewBox="0 0 12 12">
      <circle cx="6" cy="6.4" r="4.6" fill="none" stroke="#0b4f96" stroke-width="1.4"/>
      <path d="M3.6 6.2 5.6 8.2 11 2.2" fill="none" stroke="#0b4f96" stroke-width="1.6"/>
    </symbol>
    <symbol id="home-pin" viewBox="0 0 16 16">
      <circle cx="8" cy="8" r="7" fill="none" stroke="#fff" stroke-width="1.3"/>
      <path d="M4.5 8.2 8 5l3.5 3.2V11.5H9.2V9.3H6.8v2.2H4.5z" fill="#fff"/>
    </symbol>
  </defs>
</svg>

<section class="sheet sheet--front">
  <div class="photo hero" role="img" aria-label="White three-storey office building with blue entrance, palm trees and hedges under a blue sky"></div>
  <h1 class="headline"><span class="headline__small">FOR</span><span class="headline__big">LEASE</span></h1>
  <svg class="front-shapes" viewBox="0 0 534 110" preserveAspectRatio="none">
    <polygon points="0,0 289,0 278,31 0,31" fill="#2d5fa6"/>
    <rect x="0" y="31" width="534" height="3" fill="#fff"/>
    <polygon points="286,34 534,34 534,104 258,104" fill="#5d5f63"/>
    <polygon points="0,34 286,34 258,104 0,104" fill="#1f4f98"/>
  </svg>
  <h2 class="info-title">Building Information:</h2>
  <table class="specs">
    <tr><th>Building Size:</th><td>38,485 SF</td></tr>
    <tr><th>Vacant Space:</th><td>26,878 SF</td></tr>
    <tr><th>1<sup>st</sup> and 2<sup>nd</sup> floor sizes:</th><td>about 15,500 each</td></tr>
  </table>
  <p class="front-address"><svg width="15" height="15"><use href="#home-pin"/></svg>4817 E. Calloway Ave., Lauderhill, FL 33319</p>
  <div class="strip">
    <svg viewBox="0 0 534 121" preserveAspectRatio="none">
      <defs>
        <linearGradient id="g-street" x1="0" y1="0" x2="0" y2="1">
          <stop offset="0" stop-color="#7fb0e0"/><stop offset=".35" stop-color="#eef1f4"/><stop offset=".6" stop-color="#dfe3e7"/><stop offset="1" stop-color="#5c6066"/>
        </linearGradient>
        <linearGradient id="g-aerial" x1="0" y1="0" x2="0" y2="1">
          <stop offset="0" stop-color="#5f7b45"/><stop offset=".4" stop-color="#eceff2"/><stop offset=".7" stop-color="#5c6066"/><stop offset="1" stop-color="#4f6a3a"/>
        </linearGradient>
      </defs>
      <polygon role="img" aria-label="Building facade and parking lot" points="0,0 179,0 146,121 0,121" fill="url(#g-street)"/>
      <polygon role="img" aria-label="Aerial view of building and surrounding trees" points="184,0 370,0 336,121 151,121" fill="url(#g-aerial)"/>
      <polygon role="img" aria-label="Aerial front view of building with parking" points="375,0 534,0 534,121 341,121" fill="url(#g-aerial)"/>
    </svg>
  </div>
  <div class="front-contact">
    <p class="front-contact__item front-contact__phone">
      <svg width="20" height="20" viewBox="0 0 20 20"><circle cx="10" cy="10" r="8.8" fill="none" stroke="#0b4f96" stroke-width="1.5"/><path d="M7 5.2l1.6 2.5-1 1.2c.7 1.5 1.8 2.6 3.3 3.3l1.2-1 2.5 1.6-.8 1.8c-3.8-.3-6.9-3.4-7.2-7.2z" fill="#0b4f96"/></svg>
      561-555-0148
    </p>
    <p class="front-contact__item front-contact__email">
      <svg width="16" height="16" viewBox="0 0 16 16"><circle cx="8" cy="8" r="7" fill="none" stroke="#0b4f96" stroke-width="1.3"/><rect x="4.3" y="5.3" width="7.4" height="5.4" fill="none" stroke="#0b4f96" stroke-width="1"/><path d="M4.3 5.5 8 8.4l3.7-2.9" fill="none" stroke="#0b4f96" stroke-width="1"/></svg>
      leon@dorvelholdings.com
    </p>
  </div>
</section>

<section class="sheet sheet--back">
  <div class="photo col-left top-left" role="img" aria-label="Close view of white building windows beside palm trunks"></div>
  <div class="photo photo--aerial top-right" role="img" aria-label="Aerial view of the office building with parking lot"></div>
  <div class="col-left title-block">
    <h1 class="title-block__heading">FOR<br>LEASE</h1>
    <div class="title-block__rule"></div>
    <p class="title-block__address"><svg width="16" height="16" style="flex:none;margin-top:1px"><use href="#home-pin"/></svg><span>4817 E. Calloway<br>Avenue, Lauderhill,<br>FL 33319</span></p>
  </div>
  <div class="photo col-left mid-left" role="img" aria-label="Building corner with blue entrance tower and parked vehicles"></div>
  <div class="col-left brand-block">
    <p class="brand-name">Dorvel Holdings Realty</p>
    <p class="brand-block__phone">561-555-0148</p>
    <p class="brand-block__email">leon@dorvelholdings.com</p>
  </div>
  <div class="features">
    <h2 class="features__title">MARKETING INFORMATION<br>AND FEATURES:</h2>
    <ul class="features__list">
      <li><svg width="12" height="12"><use href="#tick"/></svg><span>New landlord just purchased the building and is moving into 3rd floor space.</span></li>
      <li><svg width="12" height="12"><use href="#tick"/></svg><span>New tenants are actively moving into the building.</span></li>
      <li><svg width="12" height="12"><use href="#tick"/></svg><span>Can accommodate a tenant up to 26,000 SF.</span></li>
      <li><svg width="12" height="12"><use href="#tick"/></svg><span>Located right on Calloway Avenue and a few blocks away from busiest intersection in all of Broward County, Calloway and 441.</span></li>
      <li><svg width="12" height="12"><use href="#tick"/></svg><span>Parking ratio over 5 per 1,000 SF including secured, private parking in rear of building.</span></li>
      <li><svg width="12" height="12"><use href="#tick"/></svg><span>Building undergoing upgrades both exterior and interior:
        <ul class="features__sub">
          <li>New Landscaping</li>
          <li>New exterior paint</li>
          <li>Upgraded common area hallways</li>
          <li>Upgraded common area bathrooms</li>
          <li>New security card access system for building</li>
        </ul></span></li>
      <li><svg width="12" height="12"><use href="#tick"/></svg><span>Negotiable tenant improvement allowances.</span></li>
      <li><svg width="12" height="12"><use href="#tick"/></svg><span>Competitive rental rates.</span></li>
      <li><svg width="12" height="12"><use href="#tick"/></svg><span>On-site management.</span></li>
      <li><svg width="12" height="12"><use href="#tick"/></svg><span>Can accommodate professional or medical offices.</span></li>
    </ul>
  </div>
  <div class="photo bottom-right" role="img" aria-label="Street-level view of the building with palm trees and parked SUV"></div>
</section>
</body>
</html>
```